Website design for recruitment solutions

We connect top talents to fast growing employers in Asia. We need to revamp our existing website (currently outdated) and also add more pages to make it more informative for talents and employers.
We need final design output to be for both desktop and mobile devices. The final design output must come with all specifications so it's easier for our dev team to implement. We have a detailed mockup but we expect the design to be significantly changed by the final output. We want the pages to look aesthetic, modern and professional.
Number of Pages Required
5+ page
Requirements
Must have
- - To have Pages design for desktop+mobile. Need to take into account intermediate resolutions like 1365px\1023px\767px\479px, especially if mobile/desktop design differs considerably. Design should be repeatable (between pages), suitable for block-layout.
Nice to have
- In terms of receiving files, we usually work with designers who can deliver files in Figma or Sketch with export to Figma. If in PSD format - please export to Zeplin or Avocode, otherwise will be difficult to open

```html
<!DOCTYPE html>
<html lang="en">
<head>
<meta charset="utf-8">
<title>Talvera — Recruitment</title>
<link href="https://fonts.googleapis.com/css2?family=Montserrat:wght@400;500;600;700&family=Open+Sans:wght@400;600&display=swap" rel="stylesheet">
<style>
:root{
  --blue:#5b7199;
  --blue-dark:#4a5f86;
  --red:#e4252e;
  --ink:#2f3440;
  --muted:#7a808c;
  --line:#e3e6ec;
  --soft:#f3f4f6;
  --footer:#2a2c31;
  --white:#ffffff;
}
*{box-sizing:border-box;margin:0;padding:0}
html,body{width:1200px;height:4560px;overflow:hidden}
body{font-family:'Open Sans',sans-serif;color:var(--ink);background:var(--white);position:relative}
h1,h2,h3,h4,.brand,.btn,.nav a{font-family:'Montserrat',sans-serif}
section,header,footer{position:absolute;left:0;width:1200px;overflow:hidden}
.abs{position:absolute}
.btn{display:inline-flex;align-items:center;justify-content:center;font-size:14px;font-weight:600;border-radius:3px;height:44px;padding:0 26px}
.btn-outline{border:1px solid #b9c6d8;color:var(--blue);background:var(--white)}
.btn-red{background:var(--red);color:var(--white)}
.btn-ghost{border:1px solid rgba(255,255,255,.7);color:var(--white)}

/* hero */
.hero{top:0;height:660px;background:var(--blue)}
.hero-map{left:0;top:0;width:620px;height:660px;background:radial-gradient(ellipse at 40% 45%,rgba(255,255,255,.10),rgba(255,255,255,0) 70%)}
.hero-photo{left:600px;top:0;width:600px;height:660px;background:linear-gradient(120deg,#3d4a5e,#6f7f95 45%,#c9c9c4 80%,#e6e2da)}
.brand{color:var(--white);font-size:30px;font-weight:700;left:80px;top:40px}
.nav{right:80px;top:44px;display:flex;align-items:center;gap:40px}
.nav a{color:var(--white);font-size:14px;text-decoration:none;font-weight:500}
.nav .signup{background:var(--red);padding:10px 22px;border-radius:3px}
.nav .login{background:#1e2028;padding:10px 22px;border-radius:3px;margin-left:-26px}
.hero h1{left:80px;top:244px;width:640px;color:var(--white);font-size:36px;line-height:46px;font-weight:700;z-index:2}
.hero-form{left:80px;top:416px;display:flex}
.hero-form .field{width:210px;height:48px;background:var(--white);border-radius:3px 0 0 3px;font-size:13px;color:#a5abb5;padding:15px 18px}
.hero-form .btn{height:48px;border-radius:0 3px 3px 0;padding:0 24px}

/* process */
.process{top:660px;height:540px;background:var(--soft);text-align:center}
.process h2{left:0;width:1200px;top:80px;font-size:28px;line-height:40px;font-weight:600}
.steps{left:200px;top:196px;width:800px;display:flex;justify-content:space-between}
.step{width:180px}
.step svg{width:64px;height:64px}
.step h4{font-size:15px;color:var(--blue);margin:14px 0 10px;font-weight:600}
.step p{font-size:12px;line-height:18px;color:var(--muted)}
.process .btn{position:absolute;left:518px;top:404px}

/* smart connections */
.smart{top:1200px;height:660px;background:var(--white)}
.dash{left:-20px;top:80px;width:530px;height:420px;border-radius:8px;background:linear-gradient(160deg,#ffffff,#eef1f6);box-shadow:0 10px 30px rgba(40,50,70,.12)}
.phone{left:360px;top:260px;width:210px;height:370px;border-radius:18px;background:linear-gradient(180deg,#ffffff 55%,#f6b6c4 75%,#ee5a86);box-shadow:0 10px 30px rgba(40,50,70,.18)}
.smart h2{left:652px;top:212px;font-size:26px;font-weight:600}
.smart p{left:652px;top:260px;width:380px;font-size:14px;line-height:24px;color:var(--muted)}
.smart .btn{position:absolute;left:652px;top:404px}

/* jobs */
.jobs{top:1860px;height:500px;background:var(--white)}
.jobs h2{left:0;width:1200px;text-align:center;top:58px;font-size:28px;font-weight:600}
.card{top:128px;width:330px;height:250px;border-radius:6px;box-shadow:0 4px 22px rgba(40,50,70,.12);background:var(--white);padding:26px 28px 26px 40px;border-left:4px solid var(--blue)}
.card .meta{display:flex;justify-content:space-between;font-size:11px;color:#9aa0aa}
.card .tag{background:#e8edf5;color:var(--blue);padding:3px 9px;border-radius:3px}
.card h3{font-size:18px;font-weight:600;margin-top:18px}
.card .co{font-size:12px;color:var(--muted);margin-top:6px}
.card p{font-size:12px;line-height:19px;color:var(--muted);margin-top:18px}
.card .foot{position:absolute;left:40px;right:28px;bottom:22px;display:flex;justify-content:space-between;font-size:11px;color:#9aa0aa}
.jobs .btn{position:absolute;left:494px;top:402px;height:40px}

/* insights */
.insights{top:2400px;height:480px}
.insights .panel{left:0;top:0;width:600px;height:480px;background:var(--blue)}
.insights .photo{left:600px;top:0;width:600px;height:480px;background:linear-gradient(135deg,#5a6170,#9aa0a8 40%,#d9d8d2 75%,#b5b0a6)}
.insights h2{left:80px;top:112px;color:var(--white);font-size:28px;font-weight:600}
.insights p{left:80px;top:166px;width:440px;color:#e6ebf3;font-size:14px;line-height:24px}
.insights .btn{position:absolute;left:80px;top:310px;height:40px}

/* people first */
.people{top:2920px;height:960px;background:var(--white)}
.people h2{left:0;width:1200px;text-align:center;top:44px;font-size:28px;font-weight:600}
.people .intro{left:270px;top:92px;width:660px;text-align:center;font-size:13px;line-height:22px;color:var(--muted)}
.quote-mark{font-family:'Montserrat',sans-serif;font-size:60px;line-height:60px;color:#c9ced8;font-weight:700}
.q1{left:80px;top:160px;width:460px}
.q1 p{font-size:22px;line-height:32px;color:#4f5563;margin-top:6px}
.q1 a{display:block;margin-top:24px;font-size:12px;color:var(--blue);text-decoration:none}
.ph-lg{left:660px;top:160px;width:460px;height:500px;background:linear-gradient(150deg,#c9c3b8,#8d8b86 50%,#4f5157)}
.ph-lg .overlay{position:absolute;left:0;top:0;width:250px;height:300px;background:rgba(91,113,153,.82);padding:90px 28px 0}
.ph-lg .overlay .quote-mark{color:rgba(255,255,255,.6)}
.ph-lg .overlay p{color:var(--white);font-size:14px;line-height:22px}
.ph-lg .overlay a{display:block;margin-top:8px;font-size:11px;color:var(--white);text-decoration:underline}
.ph-md{left:80px;top:452px;width:512px;height:330px;background:linear-gradient(140deg,#5d6470,#a7a59f 45%,#dcd8cf 80%)}
.ph-sm{left:660px;top:680px;width:190px;height:220px;background:linear-gradient(160deg,#e3ddd3,#b9ada0 60%,#8f8379)}
.q2{left:872px;top:690px;width:250px}
.q2 p{font-size:14px;line-height:22px;color:#4f5563}
.q2 a{display:block;margin-top:16px;font-size:12px;color:var(--blue);text-decoration:none}

/* mission */
.mission{top:3940px;height:240px;background:var(--blue)}
.mission h2{left:80px;top:72px;width:460px;color:var(--white);font-size:28px;line-height:38px;font-weight:600}
.mission-form{left:612px;top:84px;display:flex}
.mission-form .field{width:290px;height:44px;background:var(--white);border-radius:3px;font-size:13px;color:#a5abb5;padding:13px 18px}
.mission-form .btn{margin-left:8px;border-radius:3px}
.mission .cta{left:920px;top:152px;color:#dfe5ef;font-size:12px;display:flex;align-items:center;gap:6px}

/* footer */
.site-footer{top:4180px;height:380px;background:var(--footer);color:#b9bcc4}
.site-footer .brand{position:absolute;left:80px;top:40px;font-size:22px}
.about{left:80px;top:88px;width:420px;font-size:12px;line-height:20px}
.social{left:80px;top:170px;display:flex;gap:12px}
.social span{width:34px;height:34px;border-radius:50%;background:var(--blue);display:block}
.site-footer h4{left:612px;top:44px;color:var(--white);font-size:15px;font-weight:600}
.links{top:88px;font-size:12px;line-height:26px}
.links a{display:block;color:#b9bcc4;text-decoration:none}
.addr{top:300px;width:300px;font-size:11px;line-height:18px}
.copy{left:80px;top:314px;font-size:11px}
</style>
</head>
<body>

<header class="hero">
  <div class="abs hero-map" role="img" aria-label="Faint dotted world map pattern"></div>
  <div class="abs hero-photo" role="img" aria-label="Photo of a smiling professional at a laptop with a coffee cup"></div>
  <div class="abs brand">Talvera</div>
  <nav class="abs nav">
    <a href="#">How we work</a><a href="#">Browse Jobs</a><a href="#">Employers</a><a href="#">About</a>
    <a href="#" class="signup">Sign Up</a><a href="#" class="login">Login</a>
  </nav>
  <h1 class="abs">We connect top talents<br>into fast growing employers<br>in Asia.</h1>
  <div class="abs hero-form"><div class="field">Enter your email</div><span class="btn btn-red">Get Started</span></div>
</header>

<section class="process">
  <h2 class="abs">Maximum transparency and feedback<br>throughout the process</h2>
  <div class="abs steps">
    <div class="step">
      <svg viewBox="0 0 64 64"><circle cx="32" cy="34" r="20" fill="#f6c453"/><circle cx="24" cy="30" r="7" fill="#5b7199"/><circle cx="40" cy="30" r="7" fill="#e4252e"/><path d="M16 50h32" stroke="#2f3440" stroke-width="3"/></svg>
      <h4>Matching</h4><p>Quis aute irure dolor reprehenderit in voluptate velit cillum dolore eu fugiat nulla pariatur.</p>
    </div>
    <div class="step">
      <svg viewBox="0 0 64 64"><rect x="14" y="12" width="36" height="42" rx="3" fill="#ffffff" stroke="#5b7199" stroke-width="3"/><path d="M22 24h20M22 32h20M22 40h12" stroke="#e4252e" stroke-width="3"/></svg>
      <h4>Role Briefing</h4><p>Quis aute irure dolor reprehenderit in voluptate velit cillum dolore eu fugiat nulla pariatur.</p>
    </div>
    <div class="step">
      <svg viewBox="0 0 64 64"><rect x="10" y="30" width="44" height="24" rx="3" fill="#5b7199"/><circle cx="32" cy="20" r="10" fill="#f6c453"/><path d="M26 42l5 5 9-10" stroke="#ffffff" stroke-width="3" fill="none"/></svg>
      <h4>Submit &amp; Interview</h4><p>Quis aute irure dolor reprehenderit in voluptate velit cillum dolore eu fugiat nulla pariatur.</p>
    </div>
    <div class="step">
      <svg viewBox="0 0 64 64"><path d="M12 38l14-14 10 10 16-16" stroke="#5b7199" stroke-width="4" fill="none"/><circle cx="44" cy="44" r="10" fill="#e4252e"/><path d="M39 44l4 4 6-7" stroke="#ffffff" stroke-width="2.5" fill="none"/></svg>
      <h4>Offering</h4><p>Quis aute irure dolor reprehenderit in voluptate velit cillum dolore eu fugiat nulla pariatur.</p>
    </div>
  </div>
  <span class="btn btn-outline">Explore our process</span>
</section>

<section class="smart">
  <div class="abs dash" role="img" aria-label="Desktop dashboard screen showing candidate list and score charts"></div>
  <div class="abs phone" role="img" aria-label="Mobile screen titled My Dashboard with a pink area chart"></div>
  <h2 class="abs">Smart Connections</h2>
  <p class="abs">So the quality of the connection that makes our role matching algorithm and talent managers work around the clock to find opportunities suitable to your unique profile.</p>
  <span class="btn btn-outline">Explore More</span>
</section>

<section class="jobs">
  <h2 class="abs">More than 700 Job Offers</h2>
  <div class="abs card" style="left:-108px">
    <div class="meta"><span class="tag">Full time</span><span>20 Jan, 2020</span></div>
    <h3>Full Stack Developer</h3><div class="co">Fintech Startup – Hong Kong</div>
    <p>Lorem ipsum dolor sit amet, consectetur adipiscing elit, sed do eiusmod tempor.</p>
    <div class="foot"><span>1 hr ago</span><span>›</span></div>
  </div>
  <div class="abs card" style="left:252px">
    <div class="meta"><span class="tag">Full time</span><span>20 Jan, 2020</span></div>
    <h3>Macro trading assistant</h3><div class="co">Hedge Fund – Singapore</div>
    <p>Lorem ipsum dolor sit amet, consectetur adipiscing elit, sed do eiusmod tempor.</p>
    <div class="foot"><span>1 hr ago</span><span>›</span></div>
  </div>
  <div class="abs card" style="left:612px">
    <div class="meta"><span class="tag">Full time</span><span>20 Jan, 2020</span></div>
    <h3>Consumer LS analyst</h3><div class="co">Consulting – Singapore</div>
    <p>Lorem ipsum dolor sit amet, consectetur adipiscing elit, sed do eiusmod tempor.</p>
    <div class="foot"><span>1 hr ago</span><span>›</span></div>
  </div>
  <div class="abs card" style="left:972px">
    <div class="meta"><span class="tag">Full time</span><span>20 Jan, 2020</span></div>
    <h3>Quant Developer (Python)</h3><div class="co">HFT Prop Trading – Hong Kong</div>
    <p>Lorem ipsum dolor sit amet, consectetur adipiscing elit, sed do eiusmod tempor.</p>
    <div class="foot"><span>1 hr ago</span><span>›</span></div>
  </div>
  <span class="btn btn-outline">Show All Opportunities</span>
</section>

<section class="insights">
  <div class="abs panel"></div>
  <div class="abs photo" role="img" aria-label="Photo of two colleagues reviewing documents in an office"></div>
  <h2 class="abs">Critical Insights</h2>
  <p class="abs">Our close interactions with candidates and employers have helped us create a comprehensive database of companies, talents and skills. With Talvera, you will gain full access to timely intel to help you make the right career decision.</p>
  <span class="btn btn-ghost">Explore more</span>
</section>

<section class="people">
  <h2 class="abs">People first</h2>
  <p class="abs intro">We take the time to really understand you holistically as a person to maximise your potential. As your career consultant, we provide maximum transparency and feedback throughout the process.</p>
  <div class="abs q1">
    <div class="quote-mark">“</div>
    <p>Duis aute irure dolor in reprehenderit in voluptate velit esse cillum dolore fugiat nulla pariatur. Excepteur occaecat cupidatat non proident</p>
    <a href="#">Warren Grafton</a>
  </div>
  <div class="abs ph-lg" role="img" aria-label="Photo of a woman writing notes at a desk">
    <div class="overlay"><div class="quote-mark">“</div><p>Duis aute irure dolor in repre henderit in voluptate velit esse cillum dolore fugiat nulla pariatur. Excepteur occaecat cupidatat non.</p><a href="#">Read more</a></div>
  </div>
  <div class="abs ph-md" role="img" aria-label="Photo of a team meeting around a table"></div>
  <div class="abs ph-sm" role="img" aria-label="Photo of a smiling woman in a bright room"></div>
  <div class="abs q2">
    <div class="quote-mark">“</div>
    <p>Duis aute irure dolor in repre henderit in voluptate velit esse cillum dolore...</p>
    <a href="#">Lena Olsen</a>
  </div>
</section>

<section class="mission">
  <h2 class="abs">We are on a mission to disrupt the world of recruitment.</h2>
  <div class="abs mission-form"><div class="field">Your email</div><span class="btn btn-red">Join us today</span></div>
  <div class="abs cta">Let's talk
    <svg width="30" height="16" viewBox="0 0 30 16"><path d="M2 14C10 14 20 10 28 2M22 2h6v6" stroke="#dfe5ef" stroke-width="1.5" fill="none"/></svg>
  </div>
</section>

<footer class="site-footer">
  <div class="brand">Talvera</div>
  <p class="abs about">Talvera is a modern recruitment partner for high potential technology and finance talents. We work closely with hedge funds, quant firms and fintech employers across Asia.</p>
  <div class="abs social"><span></span><span></span></div>
  <h4 class="abs">Quick Links</h4>
  <div class="abs links" style="left:612px"><a href="#">How We Work</a><a href="#">Browse Jobs</a></div>
  <div class="abs links" style="left:788px"><a href="#">Why Talvera</a></div>
  <div class="abs links" style="left:964px"><a href="#">Working @ Talvera</a><a href="#">About Talvera</a></div>
  <p class="abs copy">Talvera 2020–2025 All rights reserved</p>
  <p class="abs addr" style="left:436px">Talvera Ltd, 42 Queensway Road,<br>Unit 12B, Admiralty, Hong Kong</p>
  <p class="abs addr" style="left:792px">Talvera Pte Ltd, 18 Harbourfront Lane<br>#07-02, Singapore 098611</p>
</footer>

</body>
</html>
```